Wholesale Catalogue Design for Greeting Cards

Wren Ink is a small letterpress printery, I would like to have a wholesale catalogue designed for my range of letterpress greeting cards. I currently have 30 cards in my collection, I can supply photos, I want to be able to add to the catalogue in the future. I also want the design to represent my card designs: fun, colourful and with an elegant edge, featuring a mix of my original illustrations and hand lettering along with downloadable designs and fonts.
I would like to be able to email the catalogue to my wholesale customers and to be able to print the catalogue to use with new/potential wholesale customers.

Target Market(s)

Small boutique retailers, gift shops, baby/kids gift shops, florists

Industry/Entity Type

Wholesale

Font styles to use
Serif

Colors
eea4c8

Requirements
Must have
• I have been using baskerville font in my branding, so it would be good to include this in the design. I can provide photos and text. I also have a pink and black logo (seen attached), it would be great if the design can incorporate some of the same colour scheme.
Nice to have
• I have added some pics below of other catalogues I like the layout of.
• You can also view my work at craftlane.com/wrenink or wreninkdesign.com
• * I believe I have now loaded all the relevant photos and info
• ** I have uploaded some pics of my attempt at a wholesale catalogue and my current order sheet as this outlines the products I want in the catalogue and the different card sections. my catalogue attempt has more recent photos. I will upload photos of the remaining products by end of today (27.2.16)

```html
<!DOCTYPE html>
<html lang="en">
<head>
<meta charset="utf-8">
<title>Wren Ink Design – Wholesale Catalogue Back Cover</title>
<link rel="stylesheet" href="https://fonts.googleapis.com/css2?family=Libre+Baskerville:wght@400;700&family=Source+Sans+3:wght@400&display=swap">
<style>
  :root {
    --paper: #ffffff;
    --blush: #e8b0b1;
    --ink: #000000;
    --logo-pink: #f2a9ac;
    --logo-panel: #fafafa;
    --contact-text: #1a1a1a;
    --label-white: #ffffff;
  }
  html, body {
    margin: 0;
    padding: 0;
    overflow: hidden;
    background: var(--paper);
  }
  .cover {
    position: relative;
    width: 1200px;
    height: 848px;
    overflow: hidden;
    background: var(--paper);
  }
  .cover__shapes {
    position: absolute;
    inset: 0;
  }
  .shape-band { fill: var(--ink); }
  .shape-panel { fill: var(--blush); }

  .brand-mark {
    position: absolute;
    left: 575px;
    top: 111px;
    width: 560px;
    height: 161px;
    background: var(--logo-panel);
    display: flex;
    align-items: center;
    justify-content: center;
  }
  .brand-mark__name {
    font-family: "Libre Baskerville", "Baskerville", serif;
    font-weight: 400;
    font-size: 64px;
    letter-spacing: 1px;
    color: var(--logo-pink);
    margin: 0;
  }

  .contact {
    position: absolute;
    left: 153px;
    top: 606px;
    margin: 0;
    font-style: normal;
  }
  .contact__company {
    font-family: "Libre Baskerville", "Baskerville", serif;
    font-weight: 700;
    font-size: 20px;
    color: var(--label-white);
    margin: 0 0 2px;
    letter-spacing: 0.3px;
  }
  .contact__line {
    font-family: "Source Sans 3", "Myriad Pro", sans-serif;
    font-size: 18px;
    line-height: 24px;
    color: var(--contact-text);
    margin: 0;
  }
</style>
</head>
<body>
  <main class="cover">
    <svg class="cover__shapes" width="1200" height="848" viewBox="0 0 1200 848" aria-hidden="true">
      <polygon class="shape-band" points="0,0 286,0 936,657 750,848 0,848"/>
      <polygon class="shape-panel" points="0,0 262,0 914,657 732,848 0,848"/>
    </svg>

    <div class="brand-mark">
      <p class="brand-mark__name">Wren Ink</p>
    </div>

    <address class="contact">
      <p class="contact__company">WREN INK DESIGN</p>
      <p class="contact__line">42 Larkspur Cres.</p>
      <p class="contact__line">Coral Bay, WA&nbsp;&nbsp;&nbsp;6701</p>
      <p class="contact__line">Tel: +61(0) 400512368</p>
      <p class="contact__line">www.wrenink.com.au</p>
      <p class="contact__line">hello@wreninkdesign.com</p>
    </address>
  </main>
</body>
</html>
```